Butcher shop

We have 2 butcher shops:

Shop 9, Ridgeway Court, Aberdeen NSW 2336
Ph 02 6512 3840

47 Marlow St, Scone NSW 2337
Ph 02 6518 2274

ABN 48 907 215 816

I would like this info on reverse of card and my personal info on front of card. I have a logo I would like to use also. Require a very smooth thick matte card, with colour both sides.

Front of card should say:

Linda Farrugia
Accounts

Ph 0437 620 915
E lindafarrugia@quollmail.com.au

Industry/Entity Type

Shop

Contact Information for Business Card

Linda Farrugia
Ph 0437 620 915

Logo Text

Farrugia's Quality Meats

Logo styles of interest
Pictorial/Combination Logo
Requirements
Must have
• We use Century Gothic Font

```html
<!DOCTYPE html>
<html lang="en">
<head>
<meta charset="utf-8">
<title>Farrugia's Quality Meats – Branches</title>
<link rel="stylesheet" href="https://fonts.googleapis.com/css2?family=Didact+Gothic&display=swap">
<style>
  :root {
    --card-light: #e6dab4;
    --card-mid: #d9c897;
    --card-dark: #c8b47e;
    --ink: #141414;
    --brand-ink: #1b2a33;
    --divider: #8f8468;
    --sheen: rgba(255, 255, 255, 0.35);
  }
  html, body {
    margin: 0;
    padding: 0;
    width: 1200px;
    height: 693px;
    overflow: hidden;
    background: var(--card-mid);
  }
  .card {
    position: relative;
    width: 1200px;
    height: 693px;
    overflow: hidden;
    font-family: "Didact Gothic", "Century Gothic", sans-serif;
    color: var(--ink);
    background: radial-gradient(ellipse at 50% 40%, var(--card-light) 0%, var(--card-mid) 60%, var(--card-dark) 100%);
  }
  .card__lines {
    position: absolute;
    inset: 0;
  }
  .card__intro {
    position: absolute;
    top: 86px;
    left: 0;
    width: 1200px;
    margin: 0;
    text-align: center;
    font-size: 35px;
    font-weight: 400;
    letter-spacing: 1.5px;
  }
  .card__divider {
    position: absolute;
    left: 596px;
    top: 141px;
    width: 1px;
    height: 277px;
    background: linear-gradient(to bottom, transparent, var(--divider) 15%, var(--divider) 85%, transparent);
  }
  .branch {
    position: absolute;
    margin: 0;
    text-align: center;
    font-style: normal;
    font-size: 45px;
    line-height: 55.5px;
    letter-spacing: 1.5px;
  }
  .branch--aberdeen { left: 41px; width: 520px; top: 171px; }
  .branch--scone { left: 621px; width: 520px; top: 180px; }
  .brand {
    position: absolute;
    left: 0;
    top: 535px;
    width: 1190px;
    margin: 0;
    text-align: center;
    font-size: 37px;
    line-height: 51px;
    font-weight: 400;
    color: var(--brand-ink);
  }
</style>
</head>
<body>
  <main class="card">
    <svg class="card__lines" width="1200" height="693" viewBox="0 0 1200 693" aria-hidden="true">
      <g stroke="var(--sheen)" stroke-width="2" fill="none">
        <line x1="0" y1="380" x2="300" y2="693"/>
        <line x1="0" y1="420" x2="260" y2="693"/>
        <line x1="0" y1="460" x2="222" y2="693"/>
        <line x1="890" y1="0" x2="1200" y2="320"/>
        <line x1="930" y1="0" x2="1200" y2="280"/>
        <line x1="970" y1="0" x2="1200" y2="240"/>
      </g>
    </svg>

    <p class="card__intro">We have 2 branches:</p>

    <address class="branch branch--aberdeen">
      Shop 9, Ridgeway Court,<br>
      Aberdeen<br>
      NSW 2336<br>
      Ph 02 6512 3840
    </address>

    <div class="card__divider" aria-hidden="true"></div>

    <address class="branch branch--scone">
      47 Marlow St,<br>
      Scone<br>
      NSW 2337<br>
      Ph 02 6518 2274
    </address>

    <p class="brand">Farrugia's<br>Quality Meats</p>
  </main>
</body>
</html>
```